"Drink Champagne and Dance on the Table" sort of business card needed!

We throw events, weddings, engagement parties, baby showers and the sort of end of year corporate events that people remember long after the glitter has settled - the sort of events that make you stand still and say wow when you walk in and then make you want to "Drink Champagne and Dance on the Tables"

We have a great logo with heaps of potential and need a business card that just screams creative professionals!

We are based in Auckland, NZ and are priced at the Premium end of the market were there are around 10 other main competitors. We need to stand out and make a strong statement about who we are!

Our Business Card will be one of the few items that we print out so are fully prepared to invest in a premium print job.

We really love our logo and think it has heaps of potential! Its ok if you would like to manipulate it (maybe put it on an angle, or use the circle element on its own?).

Black and Gold is very striking, but its very done in our market so we would like to avoid a solid black background please

We have done a bit of an inspiration document to give you an idea of the sort of look and feel we are hoping to achieve.

Target Market(s)

Woman aged 30 - 45 with an income bracket of $70k +

Industry/Entity Type

Event Planning

Contact Information for Business Card

Marnie
hello@fennoriwick.co.nz
www.fennoriwick.co.nz
02734419027

Number of Pages Required

5+ page

Requirements
Must have
• Vibrant colours and design (we love the vibrant pink and gold in the inspiration file)
• We would love to see some colour and creativity (although the black and gold is very striking). Because we are doing such minimal print work I am happy for the cards to be a little more expensive so if you want to use cut outs, rounded corners, gold foil, non standard size etc I am happy for that too. I really want the wow factor.
Nice to have
• We would like the design to be double sided.
Should not have
• The logo colour changed
• Use of Purple or Green or solid black background.
• Wedding Photos!

```html
<!DOCTYPE html>
<html lang="en">
<head>
<meta charset="utf-8">
<title>Fenno Riwick — Business Card</title>
<link rel="stylesheet" href="https://fonts.googleapis.com/css2?family=Playfair+Display:wght@700&family=Arimo:wght@400;700&display=swap">
<style>
  :root {
    --backdrop: #e6e4e1;
    --card: #ffffff;
    --gold: #c9a33f;
    --gold-deep: #b38c2c;
    --gold-text: #b8902c;
    --ink-light: #ffffff;
  }
  * { box-sizing: border-box; margin: 0; padding: 0; }
  html, body {
    width: 1200px; height: 950px; overflow: hidden;
    background: var(--backdrop);
  }
  .canvas {
    position: relative; width: 1200px; height: 950px;
  }
  .card {
    position: absolute; left: 250px; width: 700px; height: 400px;
    background: var(--card);
    box-shadow: 0 10px 30px rgba(0,0,0,.18);
    overflow: hidden;
  }
  .card--back { top: 55px; }
  .card--front { top: 495px; }

  /* Back */
  .back-mark {
    position: absolute; left: 50%; top: 78px; transform: translateX(-50%);
    width: 130px; height: 130px; border-radius: 50%;
    border: 3px solid var(--gold-text);
  }
  .back-name {
    position: absolute; left: 0; right: 0; top: 225px; text-align: center;
    font-family: "Playfair Display", serif; font-weight: 700;
    font-size: 50px; color: var(--gold-text); letter-spacing: 1px;
  }
  .back-tag {
    position: absolute; left: 0; right: 0; top: 292px; text-align: center;
    font-family: "Arimo", sans-serif; font-size: 14px; letter-spacing: 6px;
    color: var(--gold-text);
  }

  /* Front */
  .brand {
    position: absolute; left: 48px; top: 32px; width: 330px;
  }
  .brand__name {
    font-family: "Playfair Display", serif; font-weight: 700;
    font-size: 44px; line-height: 1; color: var(--gold-text); letter-spacing: .5px;
  }
  .brand__tag {
    display: flex; align-items: center; gap: 10px; margin-top: 8px;
    font-family: "Arimo", sans-serif; font-size: 12px; letter-spacing: 5px;
    color: var(--gold-text); white-space: nowrap;
  }
  .brand__tag::before, .brand__tag::after {
    content: ""; flex: 1; height: 1.5px; background: var(--gold-text);
  }
  .band {
    position: absolute; left: 0; right: 0; top: 122px; height: 188px;
    background: linear-gradient(180deg, var(--gold) 0%, var(--gold-deep) 100%);
  }
  .contact {
    position: absolute; left: 48px; top: 14px; color: var(--ink-light);
    font-family: "Arimo", sans-serif;
  }
  .contact__name { font-size: 30px; font-weight: 700; margin-bottom: 14px; letter-spacing: .5px; }
  .contact__list { list-style: none; font-size: 18px; line-height: 1.55; }
  .contact__list li { display: flex; align-items: center; gap: 10px; }
  .contact__list svg { width: 16px; height: 16px; flex: none; }
  .band-mark {
    position: absolute; right: 70px; top: 18px;
    width: 152px; height: 152px; border-radius: 50%;
    border: 2px solid rgba(255,255,255,.85);
    display: flex; align-items: center; justify-content: center;
    font-family: "Playfair Display", serif; font-weight: 700;
    font-size: 20px; color: var(--ink-light); text-align: center; line-height: 1.1;
  }
</style>
</head>
<body>
<main class="canvas">

  <section class="card card--back" aria-label="Card back">
    <div class="back-mark"></div>
    <div class="back-name">Fenno Riwick</div>
    <div class="back-tag">WEDDINGS&amp;EVENTS</div>
  </section>

  <section class="card card--front" aria-label="Card front">
    <div class="brand">
      <div class="brand__name">Fenno Riwick</div>
      <div class="brand__tag">WEDDINGS&amp;EVENTS</div>
    </div>

    <div class="band">
      <div class="contact">
        <p class="contact__name">Marnie</p>
        <ul class="contact__list">
          <li>
            <svg viewBox="0 0 16 16" fill="#fff" aria-hidden="true"><path d="M3 2h3l1.5 3.5-2 1.2a8 8 0 0 0 3.8 3.8l1.2-2L14 10v3a1 1 0 0 1-1 1A12 12 0 0 1 2 3a1 1 0 0 1 1-1z"/></svg>
            02734419027
          </li>
          <li>
            <svg viewBox="0 0 16 16" fill="#fff" aria-hidden="true"><path d="M1 3h14v10H1z"/><path d="M1 3l7 5.5L15 3" fill="none" stroke="#b8902c" stroke-width="1.3"/></svg>
            hello@fennoriwick.co.nz
          </li>
          <li>
            <svg viewBox="0 0 16 16" aria-hidden="true"><circle cx="8" cy="8" r="7" fill="#fff"/><path d="M1 8h14M8 1c3 3 3 11 0 14M8 1c-3 3-3 11 0 14" fill="none" stroke="#b8902c" stroke-width="1.1"/></svg>
            www.fennoriwick.co.nz
          </li>
        </ul>
      </div>
      <div class="band-mark">Fenno<br>Riwick</div>
    </div>
  </section>

</main>
</body>
</html>
```